Healthcare Technology Company Business Card Design

Hi,

We require a new business card design thats catchy and professional.
Our target audience is healthcare professionals. See supplied artwork for our logo.

If you think its achievable please try add the tag line, not necessary however.
"Building smarter tools for every clinic and practice and deliver everyday efficiency"

We'll require the following information on the card. No need to have the subject titles but i've referenced them for your convenience.

Personal Details
Paul Dwyer
Position: Director
Phone Number - 03 9472 5836
Mobile Number - 0438 275 904
Email: firstname.lastname@mediqbay.com.au

Company Details
Suite 31, 286 Keldon Street
Eastbrook Park, Victoria
Fax: 03 8241 3975
mediqbay.com.au

Prefer a thinner design than the normal stock standard business card dimensions.
Please ensure there is adequate bleed.

Target Market(s)

Healthcare Professionals

Industry/Entity Type

Healthcare

Font styles to use
Sans Serif

Requirements
Must have
• Clean, Sharp Looks
Should not have
• Any healthcare symbols

```html
<!DOCTYPE html>
<html lang="en">
<head>
<meta charset="utf-8">
<title>MediQbay Business Card</title>
<link rel="stylesheet" href="https://fonts.googleapis.com/css2?family=Cabin:wght@400;500;600&display=swap">
<style>
  :root {
    --orange: #ff8200;
    --navy: #233150;
    --icon: #2e4068;
    --black: #000000;
    --white: #ffffff;
    --page: #ffffff;
  }
  * { box-sizing: border-box; margin: 0; padding: 0; }
  html, body {
    width: 1200px; height: 1000px; overflow: hidden;
    background: var(--page);
    font-family: "Cabin", Arial, sans-serif;
    color: var(--navy);
  }
  .card { position: absolute; left: 172px; width: 865px; }
  .card--front { top: 18px; height: 469px; background: var(--white); box-shadow: 0 2px 8px rgba(0,0,0,.25); }
  .card--back { top: 509px; height: 468px; background: var(--black); }

  .brand { position: absolute; display: flex; align-items: center; }
  .brand__dot { border-radius: 50%; background: var(--navy); flex: none; }
  .brand__name { font-weight: 600; line-height: 1; }

  .card--front .brand { left: 68px; top: 46px; gap: 14px; }
  .card--front .brand__dot { width: 58px; height: 58px; }
  .card--front .brand__name { font-size: 50px; color: var(--navy); }

  .tagline {
    position: absolute; font-variant: small-caps; font-size: 22px;
    letter-spacing: 1px; line-height: 1; white-space: nowrap;
  }
  .tagline--first { left: 156px; top: 120px; color: var(--orange); font-weight: 600; }
  .tagline--second { right: 85px; top: 147px; color: var(--navy); font-weight: 500; }

  .address {
    position: absolute; left: 551px; top: 37px; font-style: normal;
    font-variant: small-caps; font-size: 22px; letter-spacing: 1px; line-height: 26px;
    font-weight: 500; white-space: nowrap;
  }

  .band {
    position: absolute; left: 0; top: 204px; width: 100%; height: 78px;
    background: var(--orange); text-align: center; padding-left: 10px;
  }
  .band__name { font-size: 31px; font-weight: 600; letter-spacing: 1px; padding-top: 12px; line-height: 34px; }
  .band__title { font-size: 18px; letter-spacing: 6px; font-weight: 500; line-height: 24px; }

  .contact { position: absolute; display: flex; align-items: center; gap: 10px;
    font-size: 24px; font-weight: 500; letter-spacing: 1px; line-height: 1; white-space: nowrap; }
  .contact__icon {
    width: 24px; height: 24px; border-radius: 50%; background: var(--icon);
    color: var(--orange); font-size: 16px; font-weight: 400; letter-spacing: 0;
    display: flex; align-items: center; justify-content: center; flex: none;
  }
  .contact--upper { text-transform: uppercase; font-size: 23px; letter-spacing: 1.5px; }

  .card--back .brand { left: 110px; top: 152px; gap: 28px; }
  .card--back .brand__dot { width: 130px; height: 130px; background: var(--orange); }
  .card--back .brand__name { font-size: 108px; color: var(--orange); }
</style>
</head>
<body>
  <section class="card card--front">
    <div class="brand">
      <span class="brand__dot"></span>
      <span class="brand__name">MediQbay</span>
    </div>
    <p class="tagline tagline--first">Building smarter tools for every clinic and practice</p>
    <p class="tagline tagline--second">and deliver everyday efficiency</p>
    <address class="address">
      286 Keldon Street, Suite 31<br>Eastbrook Park, Victoria
    </address>

    <div class="band">
      <p class="band__name">PAUL DWYER</p>
      <p class="band__title">DIRECTOR</p>
    </div>

    <p class="contact" style="left:149px; top:328px"><span class="contact__icon">P</span>03 9472 5836</p>
    <p class="contact" style="left:149px; top:367px"><span class="contact__icon">M</span>0438 275 904</p>
    <p class="contact contact--upper" style="left:149px; top:407px"><span class="contact__icon">E</span>firstname.lastname@mediqbay.com.au</p>
    <p class="contact" style="left:454px; top:329px"><span class="contact__icon">F</span>03 8241 3975</p>
    <p class="contact contact--upper" style="left:454px; top:368px"><span class="contact__icon">W</span>mediqbay.com.au</p>
  </section>

  <section class="card card--back">
    <div class="brand">
      <span class="brand__dot"></span>
      <span class="brand__name">MediQbay</span>
    </div>
  </section>
</body>
</html>
```